Flyer design for webdesign company

create a flyer that can be printed or sent as an email. The flyer needs to be professional, modern and engaging.

Reason: opportunity for all designers to get their designs in.

Target Market(s)

business owners that do not have a website

Industry/Entity Type

It Company

Font styles to use
Sans Serif

```html
<!DOCTYPE html>
<html lang="en">
<head>
<meta charset="utf-8">
<title>Orbitsites Flyer</title>
<link rel="stylesheet" href="https://fonts.googleapis.com/css2?family=Jost:wght@400;500&family=Oswald:wght@600;700&family=Roboto+Condensed:wght@400;700&family=Open+Sans:wght@700&display=swap">
<style>
  :root {
    --orange: #f7931e;
    --blue: #0d6cb6;
    --blue-dark: #0a4e94;
    --navy: #26338a;
    --ink: #1a1a1a;
    --grey: #3a3a3a;
    --rule: #9a9a9a;
    --paper: #ffffff;
  }
  * { margin: 0; padding: 0; box-sizing: border-box; }
  html, body { width: 953px; height: 1200px; overflow: hidden; background: var(--paper); }
  .flyer { position: relative; width: 953px; height: 1200px; background: var(--paper); font-family: "Jost", sans-serif; }

  .offer-panel {
    position: absolute; left: 34px; top: 46px; width: 408px; height: 1123px;
    background: var(--orange); border-radius: 62px 0 0 62px;
  }
  .headline {
    position: absolute; left: 34px; top: 86px; width: 408px; text-align: center;
    color: #fff; font-weight: 400; font-size: 48px; line-height: 56px; letter-spacing: 0.5px;
  }
  .benefits { position: absolute; left: 62px; top: 344px; width: 370px; list-style: none; }
  .benefits li {
    position: relative; padding-left: 35px; color: var(--ink);
    font-size: 19px; line-height: 24px; margin-bottom: 11px;
  }
  .benefits svg { position: absolute; left: 0; top: 4px; }

  .warning-band {
    position: absolute; left: 23px; top: 735px; width: 429px; height: 165px;
    background: linear-gradient(90deg, var(--blue) 0%, var(--blue-dark) 100%);
    color: #fff; text-align: center; font-family: "Oswald", sans-serif; font-weight: 600;
    font-size: 33px; line-height: 48px; padding-top: 10px; letter-spacing: 0.5px;
  }
  .pricing { position: absolute; left: 34px; top: 920px; width: 408px; text-align: center; color: var(--ink); }
  .pricing-label { color: #fff; font-size: 46px; line-height: 60px; font-weight: 400; letter-spacing: 1px; }
  .pricing-amount { color: #fff; font-family: "Oswald", sans-serif; font-weight: 700; font-size: 50px; line-height: 68px; }
  .pricing-note { font-family: "Roboto Condensed", sans-serif; font-size: 28px; line-height: 38px; }

  .brand { position: absolute; left: 479px; top: 240px; width: 430px; display: flex; align-items: center; justify-content: center; gap: 12px; }
  .brand-dot { width: 26px; height: 26px; border-radius: 50%; background: var(--orange); }
  .brand-name { color: var(--orange); font-size: 38px; font-weight: 500; }
  .divider { position: absolute; left: 479px; top: 327px; width: 429px; height: 1px; background: var(--rule); }

  .daily-rate {
    position: absolute; left: 479px; top: 352px; width: 429px; text-align: center;
    color: var(--navy); font-family: "Oswald", sans-serif; font-weight: 700; font-size: 56px; line-height: 72px;
  }
  .start-link { position: absolute; left: 479px; top: 438px; width: 429px; text-align: center; color: var(--grey); font-size: 17px; }
  .call-label { position: absolute; left: 479px; top: 474px; width: 429px; text-align: center; color: var(--orange); font-size: 42px; font-weight: 400; }
  .phone { position: absolute; left: 479px; top: 522px; width: 429px; text-align: center; color: var(--grey); font-family: "Roboto Condensed", sans-serif; font-weight: 700; font-size: 46px; }

  .photo {
    position: absolute; left: 514px; top: 589px; width: 371px; height: 528px;
    background: linear-gradient(180deg, #e6c79a 0%, #d9a98a 30%, #4b9aa8 62%, #2d5a9a 85%, #8a8d93 100%);
    border-radius: 180px 180px 0 0;
  }
  .url-bar {
    position: absolute; left: 442px; top: 1115px; width: 459px; height: 54px;
    background: linear-gradient(90deg, var(--blue) 0%, var(--blue-dark) 100%);
    border-radius: 0 26px 26px 0; color: #fff; font-family: "Open Sans", sans-serif; font-weight: 700;
    font-size: 28px; line-height: 54px; padding-left: 16px; letter-spacing: 1px;
  }
</style>
</head>
<body>
<main class="flyer">
  <div class="offer-panel"></div>
  <h1 class="headline">ATTRACT MORE<br>CUSTOMERS<br>MAKE MORE<br>MONEY</h1>

  <ul class="benefits">
    <li><svg width="22" height="16" viewBox="0 0 22 16"><path d="M1 1l7 7-7 7M11 1l7 7-7 7" fill="none" stroke="#1a1a1a" stroke-width="3.5"/></svg>97% of people look online for businesses. You need a website</li>
    <li><svg width="22" height="16" viewBox="0 0 22 16"><path d="M1 1l7 7-7 7M11 1l7 7-7 7" fill="none" stroke="#1a1a1a" stroke-width="3.5"/></svg>You’re losing many customers by not having a website</li>
    <li><svg width="22" height="16" viewBox="0 0 22 16"><path d="M1 1l7 7-7 7M11 1l7 7-7 7" fill="none" stroke="#1a1a1a" stroke-width="3.5"/></svg>Beat your competition with better visibility and credibility</li>
    <li><svg width="22" height="16" viewBox="0 0 22 16"><path d="M1 1l7 7-7 7M11 1l7 7-7 7" fill="none" stroke="#1a1a1a" stroke-width="3.5"/></svg>Beautiful websites available now</li>
    <li><svg width="22" height="16" viewBox="0 0 22 16"><path d="M1 1l7 7-7 7M11 1l7 7-7 7" fill="none" stroke="#1a1a1a" stroke-width="3.5"/></svg>Smart, clean website designs ($3000 value. No extra charge)</li>
    <li><svg width="22" height="16" viewBox="0 0 22 16"><path d="M1 1l7 7-7 7M11 1l7 7-7 7" fill="none" stroke="#1a1a1a" stroke-width="3.5"/></svg>limited to only 4 websites per area.Don’t miss out!</li>
    <li><svg width="22" height="16" viewBox="0 0 22 16"><path d="M1 1l7 7-7 7M11 1l7 7-7 7" fill="none" stroke="#1a1a1a" stroke-width="3.5"/></svg>Social media setupoptions (findly &amp; friendbook)</li>
  </ul>

  <div class="warning-band">Stop wasting Money<br>on Mailers and<br>Print Advertising</div>

  <section class="pricing">
    <p class="pricing-label">PRICING</p>
    <p class="pricing-amount">ONLY $99/MONTH</p>
    <p class="pricing-note">(That’s $3.30/Day)<br>(No other costs)</p>
  </section>

  <div class="brand"><span class="brand-dot"></span><span class="brand-name">orbitsites</span></div>
  <div class="divider"></div>

  <p class="daily-rate">ONLY $3 A DAY</p>
  <p class="start-link">click here to start building your website today!</p>
  <p class="call-label">CALL TODAY</p>
  <p class="phone">1-800-555-0147</p>

  <div class="photo" role="img" aria-label="Photo of a smiling woman holding an open laptop showing a website builder"></div>
  <div class="url-bar">www.sitelaunch247.com</div>
</main>
</body>
</html>
```